Meadowlark Learning Growth Partners (MLGP)

This is a professional business card. Logo and picture are a must on the front of the card. I am an educational consultant. I have been consulting for the past three years for a company. I am now opening my own company. My goal for my consulting company is to eventually consult all over America.

Target Market(s)

Educators, schools, professionals

Industry/Entity Type

Consulting

Contact Information for Business Card

Picture/logo on front, simple modern design

Font styles to use
Serif

Colors
85abd2
0355a3
3176b5
cedeed

Requirements
Must have
• picture, logo,
• Odessa Pruitt, Ed.S
• address 5073 Cormorant ridge Dr. Nashville, TN 37940
• Cell:616-555-0148
• Office: 629-555-0172
• www.Mlgpedu.example
• pruittodessa@mailbox.example

```html
<!DOCTYPE html>
<html lang="en">
<head>
<meta charset="utf-8">
<title>Meadowlark Learning Growth Partners – Business Card</title>
<link rel="stylesheet" href="https://fonts.googleapis.com/css2?family=Montserrat:wght@600;700&family=Libre+Baskerville:wght@700&family=Open+Sans:wght@400&display=swap">
<style>
  :root {
    --navy: #0b3c82;
    --navy-deep: #08306c;
    --white: #ffffff;
    --page: #e9ecf1;
    --photo-light: #d9dde3;
    --photo-mid: #b8a58a;
    --photo-dark: #2a2c36;
    --rule-light: rgba(255,255,255,0.35);
  }
  * { margin: 0; padding: 0; box-sizing: border-box; }
  html, body { width: 1200px; height: 844px; overflow: hidden; }
  body {
    background: var(--page);
    position: relative;
    font-family: "Open Sans", Arial, sans-serif;
  }
  .card {
    position: absolute;
    top: 267px;
    width: 540px;
    height: 309px;
    overflow: hidden;
    box-shadow: 0 6px 18px rgba(0,0,0,0.18);
  }
  .card--front { left: 40px; background: var(--white); }
  .card--back  { left: 620px; background: var(--navy); }

  /* brand lockup */
  .brand { position: absolute; display: flex; align-items: center; }
  .brand__mark {
    font-family: "Montserrat", Arial, sans-serif;
    font-weight: 700;
    letter-spacing: 2px;
  }
  .brand__divider { width: 1px; align-self: stretch; margin: 0 10px; }
  .brand__name {
    font-family: "Montserrat", Arial, sans-serif;
    font-weight: 600;
    line-height: 1.08;
  }

  .card--front .brand { left: 262px; top: 60px; }
  .card--front .brand__mark { color: var(--navy); font-size: 26px; }
  .card--front .brand__divider { background: var(--navy); }
  .card--front .brand__name { color: var(--navy); font-size: 13px; }

  .portrait {
    position: absolute;
    left: 0; top: 86px;
    width: 252px; height: 223px;
    background: radial-gradient(ellipse at 45% 35%, var(--photo-mid) 0%, var(--photo-light) 45%, var(--white) 70%),
                linear-gradient(to top, var(--photo-dark) 0%, transparent 45%);
    background-blend-mode: multiply;
  }

  .info-band {
    position: absolute;
    left: 252px; top: 152px;
    width: 288px; height: 157px;
    background: var(--navy);
    padding: 20px 0 0 22px;
  }
  .person__name {
    font-family: "Libre Baskerville", Georgia, serif;
    font-weight: 700;
    font-size: 15px;
    color: var(--navy);
    background: var(--white);
    display: none;
  }
  .info-band .person {
    font-family: "Libre Baskerville", Georgia, serif;
    font-weight: 700;
    font-size: 15px;
    color: var(--white);
    margin-bottom: 10px;
  }
  .info-band .person__title { font-weight: 700; font-size: 13px; }
  .contact-list { list-style: none; }
  .contact-list li {
    display: flex; align-items: center;
    color: var(--white);
    font-size: 12.5px;
    line-height: 18px;
  }
  .contact-list svg { width: 11px; height: 11px; margin-right: 8px; flex: none; }

  .card--back .brand { left: 150px; top: 84px; }
  .card--back .brand__mark { color: var(--white); font-size: 32px; align-self: flex-end; margin-bottom: 2px; }
  .card--back .brand__divider { background: var(--rule-light); margin: 0 12px; }
  .card--back .brand__name { color: var(--white); font-size: 17px; }
  .back__rule {
    position: absolute; left: 30px; right: 30px; top: 248px;
    height: 1px; background: var(--rule-light);
  }
  .back__address {
    position: absolute; right: 30px; top: 260px;
    color: var(--white); font-size: 12px;
  }
</style>
</head>
<body>

<section class="card card--front" aria-label="Business card front">
  <div class="brand">
    <span class="brand__mark">MLGP</span>
    <span class="brand__divider"></span>
    <span class="brand__name">Meadowlark<br>Learning<br>Growth<br>Partners</span>
  </div>

  <div class="portrait" role="img" aria-label="Portrait photo of Odessa Pruitt"></div>

  <div class="info-band">
    <p class="person">Odessa Pruitt, <span class="person__title">Ed.S</span></p>
    <ul class="contact-list">
      <li>
        <svg viewBox="0 0 12 12" aria-hidden="true"><rect x="3" y="0.5" width="6" height="11" rx="1" fill="none" stroke="#fff"/><circle cx="6" cy="9.5" r="0.7" fill="#fff"/></svg>
        616-555-0148
      </li>
      <li>
        <svg viewBox="0 0 12 12" aria-hidden="true"><path d="M1 4 Q6 0 11 4 L9.5 5.5 L8 4.5 L4 4.5 L2.5 5.5 Z" fill="#fff"/><rect x="2" y="6" width="8" height="5" rx="1" fill="#fff"/></svg>
        629-555-0172
      </li>
      <li>
        <svg viewBox="0 0 12 12" aria-hidden="true"><circle cx="6" cy="6" r="5.2" fill="#fff"/><path d="M1 6 H11 M6 1 Q3 6 6 11 M6 1 Q9 6 6 11" stroke="#0b3c82" stroke-width="0.8" fill="none"/></svg>
        www.Mlgpedu.example
      </li>
      <li>
        <svg viewBox="0 0 12 12" aria-hidden="true"><rect x="0.5" y="2" width="11" height="8" fill="#fff"/><path d="M0.5 2 L6 6.5 L11.5 2" stroke="#0b3c82" fill="none"/></svg>
        pruittodessa@mailbox.example
      </li>
    </ul>
  </div>
</section>

<section class="card card--back" aria-label="Business card back">
  <div class="brand">
    <span class="brand__mark">MLGP</span>
    <span class="brand__divider"></span>
    <span class="brand__name">Meadowlark<br>Learning<br>Growth<br>Partners</span>
  </div>
  <div class="back__rule"></div>
  <p class="back__address">5073 Cormorant ridge Dr. Nashville, TN 37940</p>
</section>

</body>
</html>
```